Brightfield Yard Service and Beyond LLC

• Mowing
• Weed eating
•Edging
• hedge trimming
• landscaping
•mulching
•yard clean up
• pressure washing

Target Market(s)

Everyone

Contact Information for Business Card

Licensed and insured

Font styles to use
Serif

Colors
59FF00
82FF00
B8FF75
E3FFCB
F4FFEA
F0912C
F2A743
F7CA91
FBE8D2
FDF5EE
EE7325
F08F49
F5BC92
FAE3D3
FDF4ED
EB3D1F
EC4F4E
F09395
F8D3D4
FCEDEE
E54698
E96AAD
F1A4CE
F9D9EA
FCEFF6

```html
<!DOCTYPE html>
<html lang="en">
<head>
<meta charset="utf-8">
<title>Brightfield Yard Service and Beyond LLC – Business Card</title>
<link href="https://fonts.googleapis.com/css2?family=Oswald:wght@500;600&family=Montserrat:wght@700;800&family=Poppins:wght@500;600;700&display=swap" rel="stylesheet">
<style>
  :root {
    --page: #ece7df;
    --white: #ffffff;
    --green-deep: #0b5a12;
    --green-text: #0f6a17;
    --grass-dark: #0d5a10;
    --grass-mid: #1f8a1c;
    --grass-light: #3fa52a;
    --lawn-light: #7dbb3a;
    --lawn-dark: #3e7d1e;
    --shadow: rgba(0,0,0,0.22);
  }
  * { box-sizing: border-box; margin: 0; padding: 0; }
  html, body { width: 1200px; height: 1200px; overflow: hidden; }
  body { background: var(--page); position: relative; }

  .card {
    position: absolute;
    left: 120px;
    width: 960px;
    height: 549px;
    border-radius: 34px;
    overflow: hidden;
    background: var(--white);
    box-shadow: 0 10px 30px var(--shadow);
  }
  .card--front { top: 38px; }
  .card--back { top: 613px; }

  .card__shape { position: absolute; inset: 0; width: 100%; height: 100%; }

  .wordmark { position: absolute; text-align: center; }
  .wordmark__name {
    font-family: "Oswald", sans-serif;
    font-weight: 600;
    font-size: 104px;
    line-height: 1;
    letter-spacing: -1px;
  }
  .wordmark__sub {
    font-family: "Poppins", sans-serif;
    font-weight: 500;
    font-size: 25px;
    letter-spacing: 1px;
    margin-top: 4px;
  }
  .card--front .wordmark { left: 40px; width: 500px; top: 150px; color: var(--white); }
  .tagline {
    font-family: "Montserrat", sans-serif;
    font-weight: 800;
    font-size: 22px;
    letter-spacing: 5px;
    margin-top: 26px;
  }

  .services {
    position: absolute;
    left: 610px;
    top: 150px;
    color: var(--green-text);
    font-family: "Montserrat", sans-serif;
    list-style: none;
  }
  .services__title {
    font-weight: 800;
    font-size: 22px;
    letter-spacing: 4px;
    margin-bottom: 10px;
  }
  .services__item {
    font-weight: 800;
    font-size: 19px;
    letter-spacing: 2.5px;
    line-height: 30px;
  }

  .card--back .wordmark { left: 470px; width: 470px; top: 60px; color: var(--green-deep); }
  .card--back .wordmark__name { font-size: 92px; }

  .contact {
    position: absolute;
    left: 470px;
    width: 470px;
    top: 268px;
    text-align: center;
    color: var(--green-deep);
    font-family: "Poppins", sans-serif;
  }
  .contact__phone { font-weight: 700; font-size: 52px; line-height: 1.1; }
  .contact__line { font-weight: 600; font-size: 17px; line-height: 1.5; }
  .contact__social {
    margin-top: 18px;
    font-weight: 600;
    font-size: 19px;
    display: flex;
    justify-content: center;
    align-items: center;
    gap: 10px;
  }
  .contact__dot {
    width: 22px; height: 22px; border-radius: 50%;
    background: var(--green-deep);
  }
</style>
</head>
<body>

  <section class="card card--front">
    <svg class="card__shape" viewBox="0 0 960 549" preserveAspectRatio="none">
      <defs>
        <linearGradient id="grassFill" x1="0" y1="0" x2="1" y2="1">
          <stop offset="0" stop-color="var(--grass-light)"/>
          <stop offset="0.5" stop-color="var(--grass-mid)"/>
          <stop offset="1" stop-color="var(--grass-dark)"/>
        </linearGradient>
      </defs>
      <rect width="960" height="549" fill="url(#grassFill)" role="img" aria-label="Close-up photo of lush green grass"/>
      <path d="M 640 0 C 560 120, 660 250, 580 370 C 530 440, 500 500, 520 549 L 960 549 L 960 0 Z" fill="var(--white)"/>
    </svg>

    <div class="wordmark">
      <div class="wordmark__name">BRIGHTFIELD</div>
      <div class="wordmark__sub">YARD SERVICE AND BEYOND LLC</div>
      <div class="tagline">LICENSED AND INSURED</div>
    </div>

    <ul class="services">
      <li class="services__title">SERVICES OFFERED:</li>
      <li class="services__item">•MOWING</li>
      <li class="services__item">•WEED EATING</li>
      <li class="services__item">•EDGING</li>
      <li class="services__item">•HEDGE TRIMMING</li>
      <li class="services__item">•LANDSCAPING</li>
      <li class="services__item">•MULCHING</li>
      <li class="services__item">•YARD CLEAN UP</li>
      <li class="services__item">•PRESSURE WASHING</li>
    </ul>
  </section>

  <section class="card card--back">
    <svg class="card__shape" viewBox="0 0 960 549" preserveAspectRatio="none">
      <defs>
        <linearGradient id="lawnFill" x1="0" y1="0" x2="1" y2="1">
          <stop offset="0" stop-color="var(--lawn-dark)"/>
          <stop offset="0.45" stop-color="var(--lawn-light)"/>
          <stop offset="1" stop-color="var(--lawn-dark)"/>
        </linearGradient>
      </defs>
      <rect width="960" height="549" fill="url(#lawnFill)" role="img" aria-label="Photo of a lawn mower on freshly cut grass beside an evergreen shrub"/>
      <path d="M 480 0 C 420 110, 480 230, 420 340 C 380 420, 360 490, 370 549 L 960 549 L 960 0 Z" fill="var(--white)"/>
    </svg>

    <div class="wordmark">
      <div class="wordmark__name">BRIGHTFIELD</div>
      <div class="wordmark__sub">YARD SERVICE AND BEYOND LLC</div>
    </div>

    <div class="contact">
      <div class="contact__phone">(555) 014-2290</div>
      <div class="contact__line">hello@brightfieldyard.com – www.brightfieldyard.com</div>
      <div class="contact__line">2741 Orchard Row, Fairhaven, AZ 85000</div>
      <div class="contact__social">
        <span>FIND US ON:</span>
        <span class="contact__dot"></span>
        <span>@brightfieldyard</span>
      </div>
    </div>
  </section>

</body>
</html>
```